VORL Pty Ltd Business Card

Looking for a simple yet eye-catching double-sided business card design using my company logo on one side and contact details on the other.

Target Market(s)

Government

Industry/Entity Type

Communication Systems Engineering

Contact Information for Business Card

VORL Pty Ltd

Requirements
Nice to have
• Would be great to have a QR code so details can be scanned into contacts

```html
<!DOCTYPE html>
<html lang="en">
<head>
<meta charset="UTF-8">
<title>VORL Pty Ltd Business Card</title>
<link href="https://fonts.googleapis.com/css2?family=Montserrat:wght@400;500;700&display=swap" rel="stylesheet">
<style>
  :root {
    --page-bg: #d9d9d9;
    --dark-start: #717b82;
    --dark-end: #35424a;
    --light-card: #f1f1f1;
    --ink: #3a454d;
    --ink-soft: #6c757b;
    --paper: #fbf9f7;
  }
  * { box-sizing: border-box; margin: 0; padding: 0; }
  html, body {
    width: 1200px; height: 1200px; overflow: hidden;
    background: var(--page-bg);
    font-family: "Montserrat", sans-serif;
  }
  .canvas {
    width: 1200px; height: 1200px;
    display: flex; flex-direction: column; align-items: center; justify-content: center;
    gap: 80px;
  }
  .card {
    width: 720px; height: 410px; border-radius: 22px; position: relative;
    box-shadow: 0 10px 24px rgba(0,0,0,0.18);
  }
  .card-front {
    background: linear-gradient(100deg, var(--dark-start) 0%, var(--dark-end) 65%);
    display: flex; align-items: center; justify-content: center;
  }
  .card-back { background: var(--light-card); }

  .brand { display: flex; align-items: center; gap: 26px; }
  .brand-dot { border-radius: 50%; flex: none; }
  .brand-text { display: flex; flex-direction: column; }
  .brand-name { font-weight: 500; line-height: 0.9; letter-spacing: 2px; }
  .brand-tagline { font-weight: 400; }

  .card-front .brand-dot { width: 120px; height: 120px; background: var(--paper); opacity: 0.85; }
  .card-front .brand-name { font-size: 128px; color: var(--paper); }
  .card-front .brand-tagline { font-size: 21px; color: var(--paper); margin-top: 8px; }

  .card-back .brand {
    position: absolute; top: 44px; left: 50%; transform: translateX(-50%);
    gap: 16px;
  }
  .card-back .brand-dot { width: 64px; height: 64px; background: var(--ink); opacity: 0.75; }
  .card-back .brand-name { font-size: 70px; color: var(--ink); }
  .card-back .brand-tagline { font-size: 12px; color: var(--ink); margin-top: 4px; }

  .person { position: absolute; left: 90px; top: 235px; text-align: right; width: 260px; }
  .person-name { font-size: 28px; font-weight: 700; color: var(--ink); }
  .person-role { font-size: 16px; color: var(--ink-soft); margin-top: 4px; }

  .contact { position: absolute; left: 390px; top: 190px; color: var(--ink); font-size: 15px; }
  .contact-row { display: flex; align-items: center; gap: 10px; margin-bottom: 8px; }
  .contact-row svg { width: 14px; height: 14px; fill: var(--ink); flex: none; }
  .address { margin-top: 6px; line-height: 1.35; }
</style>
</head>
<body>
<main class="canvas">
  <section class="card card-front">
    <div class="brand">
      <span class="brand-dot"></span>
      <div class="brand-text">
        <span class="brand-name">VORL</span>
        <span class="brand-tagline">Systems Integration Solutions</span>
      </div>
    </div>
  </section>

  <section class="card card-back">
    <div class="brand">
      <span class="brand-dot"></span>
      <div class="brand-text">
        <span class="brand-name">VORL</span>
        <span class="brand-tagline">Systems Integration Solutions</span>
      </div>
    </div>

    <div class="person">
      <p class="person-name">Marcus Delaney</p>
      <p class="person-role">Founder &amp; Director</p>
    </div>

    <div class="contact">
      <div class="contact-row">
        <svg viewBox="0 0 24 24"><path d="M6.6 10.8a15 15 0 0 0 6.6 6.6l2.2-2.2c.3-.3.7-.4 1-.2 1.1.4 2.3.6 3.6.6.6 0 1 .4 1 1V20c0 .6-.4 1-1 1A17 17 0 0 1 3 4c0-.6.4-1 1-1h3.5c.6 0 1 .4 1 1 0 1.3.2 2.5.6 3.6.1.3 0 .7-.2 1z"/></svg>
        <span>(405)-555-0147</span>
      </div>
      <div class="contact-row">
        <svg viewBox="0 0 24 24"><path d="M2 5h20v14H2z M2 5l10 8 10-8" /></svg>
        <span>admin@vorl.com.au</span>
      </div>
      <div class="contact-row">
        <svg viewBox="0 0 24 24"><circle cx="12" cy="12" r="10"/></svg>
        <span>www.vorl.com.au</span>
      </div>
      <p class="address">42-44 Harlow Street Redfern<br>NSW 2016 Australia</p>
    </div>
  </section>
</main>
</body>
</html>
```